Business cards for a tribute and obituary website

Our website is called Quiet Orchard.

It is a special place online for people to remember their loved ones who have passed away, through obituaries and tributes. Friends and family can also convey their condolences on the deceased's memorial page. Celebrating the life of the deceased and remembering their legacy is very important to us – death should not be just about grieving.

We would like the card to look tasteful and modern. The design should ideally not have colours that are too bright. The logo and website URL, www.quietorchardpages.net should be visible on the front of the card, with our slogan "Celebrating a life passed" on the back.

The design should communicate our purpose – remembering loved ones who have passed – and also a lighter tone of celebrating life. It should not look like a funeral director's card!

Our logo has been attached. Looking forward to some beautiful designs! Get creative :)
Updates

Reason: Thank you all for your designs. The rest of my team and I have not reached a decision on which design to select and I am collecting feedback from them. I will provide feedback for any changes that need to be made soon. It would be great if we could see more original designs and in more colours! We will definitely select a design by this deadline.

Industry/Entity Type

Business

Contact Information for Business Card

Nadia Fenwick
Project Manager
471226809
nadiafenwick@quietorchardpages.net

Font styles to use
Serif
Sans Serif

Requirements
Must have
• Logo and website address (www.quietorchardpages.net) on the front.
Nice to have
• Hi designers! It would be nice to see alternative colours – feel free to try out colours that are tasteful and subtle. The colour of the business card does not have to be the same as the logo.
• We would also like to see the logo used in different ways, perhaps a glossy or embossed finish. The card should look stylish.

```html
<!DOCTYPE html>
<html lang="en">
<head>
<meta charset="utf-8">
<title>Quiet Orchard – Business Cards</title>
<link href="https://fonts.googleapis.com/css2?family=Arvo:wght@700&family=Gentium+Book+Plus&family=Tinos&family=Lato:wght@300;400&display=swap" rel="stylesheet">
<style>
  :root {
    --backdrop: #e9e8e6;
    --navy: #0e1f4b;
    --olive: #7c9a3a;
    --white: #ffffff;
    --url-gold: #c9c97e;
    --mark-faint: rgba(255, 255, 255, 0.16);
  }
  * { box-sizing: border-box; margin: 0; padding: 0; }
  html, body {
    width: 1200px;
    height: 960px;
    overflow: hidden;
    background: var(--backdrop);
  }
  .card-set {
    position: relative;
    width: 1200px;
    height: 960px;
  }
  .card {
    position: absolute;
    top: 120px;
    width: 420px;
    height: 720px;
    overflow: hidden;
  }
  /* Front */
  .card--front {
    left: 150px;
    background: var(--navy);
    color: var(--white);
    text-align: center;
  }
  .brand-badge {
    display: block;
    width: 150px;
    height: 150px;
    margin: 130px auto 0;
    border: 14px solid var(--white);
    border-radius: 50%;
  }
  .brand-name {
    margin-top: 34px;
    font-family: "Arvo", serif;
    font-weight: 700;
    font-size: 44px;
    line-height: 1.02;
  }
  .tagline {
    margin-top: 6px;
    font-family: "Gentium Book Plus", serif;
    font-size: 27px;
  }
  .site-url {
    position: absolute;
    left: 0;
    right: 0;
    bottom: 44px;
    font-family: "Gentium Book Plus", serif;
    font-size: 22px;
    color: var(--url-gold);
    letter-spacing: 0.3px;
  }
  /* Back */
  .card--back {
    left: 630px;
    background: var(--olive);
    color: var(--white);
  }
  .holder {
    position: absolute;
    top: 46px;
    left: 34px;
  }
  .holder-name {
    font-family: "Tinos", serif;
    font-size: 44px;
    line-height: 1;
  }
  .holder-rule {
    width: 230px;
    height: 2px;
    margin-top: 4px;
    background: var(--white);
  }
  .holder-role {
    margin: 3px 0 0 22px;
    font-family: "Lato", sans-serif;
    font-weight: 300;
    font-size: 19px;
    letter-spacing: 1.2px;
  }
  .contact-list {
    position: absolute;
    top: 148px;
    left: 34px;
    list-style: none;
    font-family: "Lato", sans-serif;
    font-weight: 300;
    font-size: 18px;
  }
  .contact-item {
    display: flex;
    align-items: center;
    gap: 8px;
    margin-bottom: 12px;
  }
  .contact-icon { width: 16px; height: 16px; flex: none; }
  .faint-mark {
    position: absolute;
    right: -60px;
    bottom: 40px;
    width: 360px;
    height: 360px;
    border: 38px solid var(--mark-faint);
    border-radius: 50%;
  }
</style>
</head>
<body>
<main class="card-set">
  <section class="card card--front" aria-label="Card front">
    <span class="brand-badge" aria-hidden="true"></span>
    <h1 class="brand-name">Quiet<br>Orchard</h1>
    <p class="tagline">Celebrating a life passed</p>
    <p class="site-url">www.quietorchardpages.net</p>
  </section>

  <section class="card card--back" aria-label="Card back">
    <div class="holder">
      <h2 class="holder-name">Nadia Fenwick</h2>
      <div class="holder-rule"></div>
      <p class="holder-role">Project Manager</p>
    </div>
    <ul class="contact-list">
      <li class="contact-item">
        <svg class="contact-icon" viewBox="0 0 16 16" aria-hidden="true">
          <circle cx="8" cy="8" r="8" fill="#fff"/>
          <path d="M5.2 4.2l1.4 1.6-.7 1c.5 1.1 1.2 1.8 2.3 2.3l1-.7 1.6 1.4-.8 1.2c-2.8-.3-5.1-2.6-5.4-5.4z" fill="#7c9a3a"/>
        </svg>
        <span>471226809</span>
      </li>
      <li class="contact-item">
        <svg class="contact-icon" viewBox="0 0 16 16" aria-hidden="true">
          <circle cx="8" cy="8" r="8" fill="#fff"/>
          <rect x="4" y="5.2" width="8" height="5.6" fill="#7c9a3a"/>
          <path d="M4 5.2l4 3 4-3" stroke="#fff" stroke-width="0.9" fill="none"/>
        </svg>
        <span>nadiafenwick@quietorchardpages.net</span>
      </li>
    </ul>
    <span class="faint-mark" aria-hidden="true"></span>
  </section>
</main>
</body>
</html>
```